Quorvix Letter head

Quorvix is a young and energetic software development consultancy. We spend our time working with clients to turn what ever is in their heads in to software.
We are trying to create an image of a high class software boutique who build class leading bespoke solutions.
We need a sharp letter head that looks great on high quality media.
We like bold colours and distinctive design. So show us what you can do.
Industry/Entity Type
Software
Requirements
Must have
- Our company is based in the UK and are requried to have on the paper somewhere the following information:
* Registered company name: Quorvix Ltd
* Registered company number
* VAT registration number
In addition we also want the following:
* An email address
* Telephone number
* Website address
An example of what some pages have in their footer is something like the following:
Quorvix Ltd is registered in England and Wales. Reg. no: 5316274
Registered office: 48 Cobblewick Road, Harlow Essex, CM93TP. Tel: 07712365081
You do not have to use this sentance but please make sure your design incorporates accommodates the requirements for UK based companies

```html
<!DOCTYPE html>
<html lang="en">
<head>
<meta charset="utf-8">
<title>Quorvix Letterhead</title>
<link rel="stylesheet" href="https://fonts.googleapis.com/css2?family=Arimo:wght@400&family=Montserrat:wght@300;400&display=swap">
<style>
  :root {
    --paper: #ffffff;
    --ink: #1e1e1e;
    --rule-dark: #2e2e2e;
    --rule-mid: #b9b9b9;
    --brand-red: #c8232c;
    --brand-red-soft: #e0737a;
    --watermark: #f3d6d8;
  }
  * { margin: 0; padding: 0; box-sizing: border-box; }
  html, body {
    width: 871px;
    height: 1200px;
    overflow: hidden;
    background: var(--paper);
  }
  .letterhead {
    position: relative;
    width: 871px;
    height: 1200px;
    background: var(--paper);
    font-family: "Arimo", Arial, sans-serif;
    color: var(--ink);
  }
  .header-rule {
    position: absolute;
    left: 0;
    width: 871px;
    background: linear-gradient(90deg, var(--rule-dark) 0%, var(--rule-mid) 42%, transparent 52%, transparent 58%, var(--rule-mid) 66%, var(--rule-dark) 100%);
  }
  .header-rule--top { top: 10px; height: 4px; }
  .header-rule--bottom { top: 76px; height: 4px; }
  .brand {
    position: absolute;
    right: 20px;
    top: 16px;
    text-align: right;
  }
  .brand-name {
    font-family: "Montserrat", sans-serif;
    font-weight: 400;
    font-size: 44px;
    line-height: 48px;
    letter-spacing: 2px;
    color: var(--brand-red);
  }
  .brand-reg {
    font-size: 8.5px;
    line-height: 10px;
    margin-top: 2px;
    color: var(--ink);
  }
  .watermark {
    position: absolute;
    left: 0;
    width: 871px;
    top: 530px;
    text-align: center;
    font-family: "Montserrat", sans-serif;
    font-weight: 300;
    font-size: 148px;
    line-height: 148px;
    letter-spacing: 6px;
    color: var(--watermark);
  }
  .footer-rule {
    position: absolute;
    left: 0;
    width: 871px;
    height: 3px;
    background: linear-gradient(90deg, var(--brand-red) 0%, var(--brand-red-soft) 55%, transparent 100%);
  }
  .footer-rule--upper { top: 1153px; }
  .footer-rule--lower { top: 1160px; height: 2px; opacity: 0.8; }
  .footer-address {
    position: absolute;
    left: 20px;
    top: 1166px;
    font-size: 13.5px;
    line-height: 17px;
  }
  .footer-contact {
    position: absolute;
    right: 20px;
    top: 1166px;
    font-size: 13.5px;
    line-height: 14px;
    text-align: right;
  }
</style>
</head>
<body>
  <main class="letterhead">
    <div class="header-rule header-rule--top"></div>
    <div class="brand">
      <div class="brand-name">QUORVIX</div>
      <div class="brand-reg">Quorvix Ltd. Reg.No. 5316274</div>
    </div>
    <div class="header-rule header-rule--bottom"></div>

    <div class="watermark" aria-hidden="true">QUORVIX</div>

    <div class="footer-rule footer-rule--upper"></div>
    <div class="footer-rule footer-rule--lower"></div>
    <address class="footer-address" style="font-style: normal;">
      Registered Office: 48 Cobblewick Road, Harlow Essex, CM93TP.<br>
      Tel No: 07712365081
    </address>
    <div class="footer-contact">
      info@quorvix.com<br>
      www.quorvix.uk
    </div>
  </main>
</body>
</html>
```